High End Business Card Design for Flooring Store

Looking for a new card design for our hardwood flooring company. We have no print budget for these and are open to cards made from wood, metal, cardstock with embossed print ... or any combination of these. No plastic.

We sell luxury products and I want the cards to reflect our image of quality and class.

Our contact information as such;
Employee Name
418 Colbrook Blvd.
Carden Falls, ON
K9R-3M5
(555) 214-3968
Employee email @velkaflooring.com

Target Market(s)

Home Builders

Contact Information for Business Card

Emnployee name, business contact information

```html
<!DOCTYPE html>
<html lang="en">
<head>
<meta charset="utf-8">
<title>Velka Flooring – Business Card</title>
<link href="https://fonts.googleapis.com/css2?family=Montserrat:wght@500;600&family=IBM+Plex+Sans:wght@400&display=swap" rel="stylesheet">
<style>
  :root {
    --page: #a6a6a6;
    --card: #ffffff;
    --maroon: #8f2a25;
    --gold: #e8b630;
    --grey-text: #5f5f5f;
    --body-text: #555555;
  }
  * { margin: 0; padding: 0; box-sizing: border-box; }
  html, body {
    width: 1161px;
    height: 1200px;
    overflow: hidden;
    background: var(--page);
  }
  .sheet {
    width: 1161px;
    height: 1200px;
    display: flex;
    flex-direction: column;
    align-items: center;
    justify-content: center;
    gap: 40px;
  }
  .card {
    position: relative;
    width: 940px;
    height: 538px;
    background: var(--card);
    overflow: hidden;
  }

  /* Front */
  .card-front .brand {
    position: absolute;
    left: 0; right: 0;
    top: 150px;
    display: flex;
    flex-direction: column;
    align-items: center;
  }
  .brand-row {
    display: flex;
    align-items: center;
    gap: 22px;
  }
  .brand-square {
    width: 74px;
    height: 74px;
    background: var(--gold);
  }
  .brand-name {
    font-family: "Montserrat", sans-serif;
    font-weight: 500;
    font-size: 158px;
    line-height: 1;
    color: var(--maroon);
    letter-spacing: 2px;
  }
  .brand-tagline {
    margin-top: 10px;
    font-family: "Montserrat", sans-serif;
    font-weight: 500;
    font-size: 37px;
    line-height: 1.15;
    color: var(--grey-text);
    text-align: center;
  }

  /* Back */
  .employee-name {
    position: absolute;
    left: 62px;
    top: 52px;
    font-family: "Montserrat", sans-serif;
    font-weight: 600;
    font-size: 37px;
    color: var(--maroon);
    letter-spacing: 0.5px;
  }
  .contact {
    position: absolute;
    left: 62px;
    font-family: "IBM Plex Sans", sans-serif;
    font-size: 20px;
    line-height: 1.5;
  }
  .contact-line {
    display: flex;
    align-items: center;
    gap: 12px;
  }
  .contact-direct { top: 162px; color: var(--body-text); }
  .contact-direct .contact-line { margin-bottom: 5px; }
  .contact-address { top: 372px; color: var(--maroon); }
  .contact-address .indent { padding-left: 22px; }
  .icon { width: 10px; height: 12px; flex: none; }

  .mini-brand {
    position: absolute;
    right: 58px;
    top: 58px;
    text-align: center;
  }
  .mini-brand-row {
    display: flex;
    align-items: center;
    gap: 6px;
  }
  .mini-brand-square {
    width: 16px;
    height: 16px;
    background: var(--gold);
  }
  .mini-brand-name {
    font-family: "Montserrat", sans-serif;
    font-weight: 500;
    font-size: 36px;
    line-height: 1;
    color: var(--maroon);
  }
  .mini-brand-tagline {
    font-family: "Montserrat", sans-serif;
    font-weight: 500;
    font-size: 9.5px;
    line-height: 1.15;
    color: var(--grey-text);
    padding-left: 22px;
  }
</style>
</head>
<body>
<main class="sheet">

  <section class="card card-front" aria-label="Card front">
    <div class="brand">
      <div class="brand-row">
        <span class="brand-square"></span>
        <span class="brand-name">Velka</span>
      </div>
      <p class="brand-tagline">Planchers &amp; Escaliers<br>Flooring &amp; Stairs</p>
    </div>
  </section>

  <section class="card card-back" aria-label="Card back">
    <h1 class="employee-name">EMPLOYEE NAME</h1>

    <div class="mini-brand">
      <div class="mini-brand-row">
        <span class="mini-brand-square"></span>
        <span class="mini-brand-name">Velka</span>
      </div>
      <p class="mini-brand-tagline">Planchers &amp; Escaliers<br>Flooring &amp; Stairs</p>
    </div>

    <div class="contact contact-direct">
      <p class="contact-line">
        <svg class="icon" viewBox="0 0 10 12" aria-hidden="true"><rect x="1.5" y="0.5" width="7" height="11" rx="1.2" fill="none" stroke="#555" stroke-width="1.2"/><rect x="4" y="9.2" width="2" height="1" fill="#555"/></svg>
        (555) 214-3968
      </p>
      <p class="contact-line">
        <svg class="icon" viewBox="0 0 10 12" aria-hidden="true"><rect x="0.5" y="3" width="9" height="6" fill="#555"/><path d="M0.5 3 L5 6.5 L9.5 3" fill="none" stroke="#fff" stroke-width="0.9"/></svg>
        info@velkaflooring.com
      </p>
    </div>

    <div class="contact contact-address">
      <p class="contact-line">
        <svg class="icon" viewBox="0 0 10 12" aria-hidden="true"><circle cx="5" cy="4" r="3" fill="none" stroke="#8f2a25" stroke-width="1.5"/><path d="M5 7 L5 9.5" stroke="#8f2a25" stroke-width="1.5"/><rect x="1" y="10" width="8" height="1.4" fill="#8f2a25"/></svg>
        418 Colbrook Blvd.
      </p>
      <p class="indent">K9R-3M5</p>
      <p class="indent">Carden Falls, ON</p>
    </div>
  </section>

</main>
</body>
</html>
```